Illustrate a statistic and its significance

Please create a graphical representation of the success rate of the Vail Procedure for our website. The Vail Procedure has a success rate of 80%. This means the procedure is successful for 8 out of every 10 people. An 80% success rate by itself is great. However, it's even more impressive when you consider that the only people we perform this procedure on are patients who have exhausted conventional treatment options for migraines and headaches. I would really like to emphasize both the success rate and the type of patients we are successful in treating with this procedure.
For example, you could create an illustration of outlines of 10 people with 8 of them shaded in, which would represent an 80% success rate. Then, underneath this image, you could add a bullet list of the types of treatments patients (such as the 10 figures in the image) have tried before coming to us/having this procedure, which include the following:
Prescription medications
Trigger point injections
Nerve blocks
Migraine surgery
Dermil
Chiropractic care
Physical therapy
Biofeedback
Massage
Acupuncture
Or maybe there is another/better way to represent this statistic graphically? I'm just looking for an effective illustration of this important statistic and its significance.
Our brand colors are red (#fd444a) and blue (#214170)
Thank you!
People who suffer from chronic migraines and headaches
Healthcare/Medical
- Athiti

```html
<!DOCTYPE html>
<html lang="en">
<head>
<meta charset="utf-8">
<title>Vail Procedure – 80% Success Rate</title>
<link rel="stylesheet" href="https://fonts.googleapis.com/css2?family=Montserrat:wght@500;800&family=Rubik:wght@400&display=swap">
<style>
  :root {
    --brand-red: #fd444a;
    --brand-blue: #214170;
    --text-navy: #1f3566;
    --page-bg: #ffffff;
  }
  html, body {
    margin: 0;
    padding: 0;
    overflow: hidden;
    background: var(--page-bg);
  }
  .canvas {
    position: relative;
    width: 1200px;
    height: 675px;
    overflow: hidden;
    background: var(--page-bg);
  }
  .stat-figure {
    position: absolute;
    inset: 0;
    width: 1200px;
    height: 675px;
  }
  .stat-number {
    font-family: "Montserrat", sans-serif;
    font-weight: 800;
  }
  .baseline-glow {
    position: absolute;
    left: 200px;
    top: 410px;
    width: 800px;
    height: 60px;
    background: radial-gradient(ellipse at center, rgba(255,255,255,0.95) 0%, rgba(255,255,255,0.85) 45%, rgba(255,255,255,0) 72%);
  }
  .brand-name {
    position: absolute;
    left: 758px;
    top: 203px;
    font-family: "Montserrat", sans-serif;
    font-weight: 500;
    font-size: 27px;
    line-height: 1;
    color: var(--brand-red);
    white-space: nowrap;
  }
  .treatment-list {
    position: absolute;
    left: 0;
    top: 456px;
    width: 1200px;
    margin: 0;
    padding: 0;
    list-style: none;
    font-family: "Rubik", sans-serif;
    font-size: 20.4px;
    line-height: 24.5px;
    color: var(--text-navy);
    text-align: center;
  }
  .treatment-row { display: block; }
  .treatment-row span + span::before {
    content: "";
    display: inline-block;
    width: 7px;
    height: 7px;
    margin: 0 9px 3px;
    border-radius: 50%;
    background: var(--brand-red);
  }
</style>
</head>
<body>
<main class="canvas">
  <svg class="stat-figure" viewBox="0 0 1200 675" role="img" aria-label="Large 80 percent figure; the digits are filled with photographs of women suffering from migraine headaches">
    <defs>
      <linearGradient id="photo-fill" x1="0" y1="0" x2="0" y2="1">
        <stop offset="0" stop-color="#e7cbb9"/>
        <stop offset="0.35" stop-color="#c9a99a"/>
        <stop offset="0.62" stop-color="#7d86a3"/>
        <stop offset="1" stop-color="#2b4a7d"/>
      </linearGradient>
    </defs>
    <text class="stat-number" x="245" y="444" font-size="440" textLength="495" lengthAdjust="spacingAndGlyphs" fill="url(#photo-fill)">80</text>
    <text class="stat-number" x="750" y="444" font-size="255" textLength="200" lengthAdjust="spacingAndGlyphs" fill="var(--brand-red)">%</text>
  </svg>

  <div class="baseline-glow"></div>

  <div class="brand-name">Kestrel Clinic</div>

  <ul class="treatment-list">
    <li class="treatment-row"><span>Prescription medications</span><span>Trigger point injections</span><span>Nerve blocks</span></li>
    <li class="treatment-row"><span>Migraine surgery</span><span>Dermil</span><span>Chiropractic care</span><span>Physical therapy</span></li>
    <li class="treatment-row"><span>Biofeedback</span><span>Massage</span><span>Acupuncture</span></li>
  </ul>
</main>
</body>
</html>
```